Ward Compass Business Card Design*

We need a business card design for our company Ward Compass. Our company is specialized in providing online consulting services regarding medical institutions, hospitals and doctors. We work with patients worldwide looking to choose between healthcare providers. We have a website you may use as a reference, where we list doctors and clinics worldwide. So we target Medical providers as well as patients worldwide.
Target Market(s)
Medical Providers and patients around the world
Industry/Entity Type
Medical
Contact Information for Business Card
Salma Derkaoui
CEO
+90 612 348 2071
info@wardcompass-example.com
www.wardcompass-example.com
14 Annakhil 3 H.R.B. Rabat, Morocco
Requirements
Must have
- Company logo/name on one full side, personal info and smaller logo and company name on the other side.
Nice to have
- Smart and elegant design

```html
<!DOCTYPE html>
<html lang="en">
<head>
<meta charset="utf-8">
<title>Ward Compass – Business Card</title>
<link href="https://fonts.googleapis.com/css2?family=Quicksand:wght@400;500;600&display=swap" rel="stylesheet">
<style>
  :root {
    --backdrop: #161616;
    --card: #2a2a2a;
    --card-edge: #333333;
    --brand-blue: #2a62c4;
    --silver: #c9c9c9;
    --text-light: #d8d8d8;
    --text-muted: #9a9a9a;
    --white: #ffffff;
  }
  * { margin: 0; padding: 0; box-sizing: border-box; }
  html, body {
    width: 1200px; height: 900px; overflow: hidden;
    background: var(--backdrop);
    font-family: "Quicksand", sans-serif;
  }
  .stage {
    position: relative; width: 1200px; height: 900px;
  }
  .card {
    position: absolute; left: 320px;
    width: 560px; height: 330px;
    background: var(--card);
    border: 1px solid var(--card-edge);
    box-shadow: 0 20px 40px rgba(0,0,0,.55);
    overflow: hidden;
  }
  .card--front { top: 90px; }
  .card--back { top: 480px; }

  /* Front: company name */
  .front-brand {
    position: absolute; inset: 0;
    display: flex; align-items: center; justify-content: center; gap: 18px;
  }
  .brand-dot {
    width: 34px; height: 34px; border-radius: 50%;
    background: var(--brand-blue);
  }
  .front-brand .brand-name {
    font-size: 44px; font-weight: 500; color: var(--silver);
    letter-spacing: 1px;
  }

  /* Back: personal info */
  .person {
    position: absolute; left: 34px; top: 30px;
  }
  .person-name {
    font-size: 22px; font-weight: 500; color: var(--text-light);
  }
  .person-name .first { color: var(--brand-blue); }
  .person-role {
    font-size: 16px; color: var(--text-muted); margin-top: 2px;
  }
  .contacts {
    position: absolute; left: 34px; top: 122px;
    list-style: none;
  }
  .contacts li {
    display: flex; align-items: center; gap: 10px;
    font-size: 13px; color: var(--text-light);
    line-height: 21px;
  }
  .contacts svg { width: 12px; height: 12px; fill: var(--brand-blue); flex: none; }

  .back-brand {
    position: absolute; left: 290px; top: 128px;
    display: flex; align-items: center; gap: 10px;
  }
  .back-brand .brand-dot { width: 22px; height: 22px; }
  .back-brand .brand-name {
    font-size: 22px; font-weight: 500; color: var(--text-light);
    letter-spacing: 1.5px; text-transform: uppercase;
  }

  .swoosh { position: absolute; left: 0; top: 0; width: 560px; height: 330px; }
  .address {
    position: absolute; right: 30px; bottom: 22px;
    text-align: right; color: var(--white);
    font-size: 15px; line-height: 21px;
  }
</style>
</head>
<body>
<main class="stage">

  <section class="card card--front" aria-label="Card front">
    <div class="front-brand">
      <span class="brand-dot"></span>
      <span class="brand-name">Ward Compass</span>
    </div>
  </section>

  <section class="card card--back" aria-label="Card back">
    <svg class="swoosh" viewBox="0 0 560 330" aria-hidden="true">
      <path d="M0,170 C50,250 260,285 560,246 L560,262 C260,300 40,275 0,212 Z" fill="#111" opacity=".6"/>
      <path d="M0,165 C45,245 255,280 560,242 C270,290 45,265 0,205 Z" fill="var(--silver)"/>
      <path d="M0,208 C55,270 270,292 560,255 L560,330 L0,330 Z" fill="var(--brand-blue)"/>
    </svg>

    <div class="person">
      <p class="person-name"><span class="first">Salma</span> Derkaoui</p>
      <p class="person-role">CEO</p>
    </div>

    <ul class="contacts">
      <li>
        <svg viewBox="0 0 24 24"><path d="M6.6 10.8a15.1 15.1 0 0 0 6.6 6.6l2.2-2.2a1 1 0 0 1 1-.25 11.4 11.4 0 0 0 3.6.57 1 1 0 0 1 1 1V20a1 1 0 0 1-1 1A17 17 0 0 1 3 4a1 1 0 0 1 1-1h3.5a1 1 0 0 1 1 1c0 1.25.2 2.45.57 3.57a1 1 0 0 1-.25 1z"/></svg>
        +90 612 348 2071
      </li>
      <li>
        <svg viewBox="0 0 24 24"><path d="M2 5h20v14H2z M4 7v.5l8 5 8-5V7z" fill-rule="evenodd"/></svg>
        info@wardcompass-example.com
      </li>
      <li>
        <svg viewBox="0 0 24 24"><circle cx="12" cy="12" r="10"/><path d="M2 12h20M12 2c3 3 3 17 0 20M12 2c-3 3-3 17 0 20" stroke="#2a2a2a" stroke-width="1.6" fill="none"/></svg>
        www.wardcompass-example.com
      </li>
    </ul>

    <div class="back-brand">
      <span class="brand-dot"></span>
      <span class="brand-name">Ward Compass</span>
    </div>

    <p class="address">14 Annakhil<br>3 H.R.B., Rabat, Morocco</p>
  </section>

</main>
</body>
</html>
```